Business Card Design

Cedar Gate Rentals
Cedar Gate Rentals is a high end home rental leasing company that provides exquisite properties in niche markets. We are a small family owned business that considers our clients not as renters, but as friends. Every property we buy must be brought up to our high standards before it is offered on the market. The properties that we lease are exceptional, "move in" ready homes. This allows for the client to take pride in their lease as if it was their own home. To put it another way; we do not lease a property that we would not live in ourselves.

Target Market(s)

Couples making $100K or more

Industry/Entity Type

Business

Requirements
Must have
• Some sort of logo
Nice to have
• good slogan
Should not have
• Pink

```html
<!DOCTYPE html>
<html lang="en">
<head>
<meta charset="utf-8">
<title>Cedar Gate Rentals – Business Card</title>
<link href="https://fonts.googleapis.com/css2?family=Ubuntu:wght@300;500;700&display=swap" rel="stylesheet">
<style>
  :root {
    --paper: #ffffff;
    --brand-blue: #1472b0;
    --brand-green: #3cac4c;
    --rule-grey: #4a4a4a;
    --ink-dark: #2b2b2b;
    --ink-body: #333333;
  }
  html, body {
    margin: 0;
    padding: 0;
    overflow: hidden;
    background: var(--paper);
  }
  .card {
    position: relative;
    width: 1200px;
    height: 687px;
    background: var(--paper);
    font-family: "Ubuntu", sans-serif;
    overflow: hidden;
  }
  .brand-mark {
    position: absolute;
    top: 22px;
    left: 562px;
    width: 84px;
    height: 84px;
  }
  .brand-name {
    position: absolute;
    top: 150px;
    left: 0;
    width: 1200px;
    margin: 0;
    text-align: center;
    font-family: "Ubuntu", sans-serif;
    font-weight: 700;
    font-size: 56px;
    line-height: 74px;
    letter-spacing: 3px;
    text-transform: uppercase;
    color: var(--brand-green);
  }
  .rule {
    position: absolute;
    height: 4px;
    background: var(--rule-grey);
  }
  .rule--long { top: 305px; left: 412px; width: 384px; }
  .rule--short { top: 385px; left: 539px; width: 104px; }
  .tagline {
    position: absolute;
    top: 329px;
    left: 0;
    width: 1200px;
    margin: 0;
    text-align: center;
    font-weight: 700;
    font-size: 32px;
    letter-spacing: 0.8px;
    color: var(--ink-dark);
  }
  .services {
    position: absolute;
    top: 419px;
    left: 37px;
    width: 1200px;
    margin: 0;
    text-align: center;
    font-weight: 300;
    font-size: 33px;
    line-height: 47px;
    letter-spacing: 0.4px;
    color: var(--ink-body);
  }
  .contact {
    position: absolute;
    top: 589px;
    margin: 0;
    font-weight: 300;
    font-size: 32px;
    line-height: 46px;
    letter-spacing: 0.3px;
    color: var(--ink-body);
  }
  .contact--person { left: 34px; }
  .contact--details { left: 766px; }
</style>
</head>
<body>
  <main class="card">
    <svg class="brand-mark" viewBox="0 0 84 84" role="img" aria-label="Cedar Gate Rentals brand mark">
      <circle cx="42" cy="42" r="38" fill="none" stroke="var(--brand-blue)" stroke-width="6"/>
    </svg>
    <h1 class="brand-name">Cedar Gate<br>Rentals</h1>
    <div class="rule rule--long"></div>
    <p class="tagline">Easy Rental. Excellent Living</p>
    <div class="rule rule--short"></div>
    <p class="services">
      Property Services, Professional Home Rental Leasing Services,<br>
      Construction Services, Property Management Services,<br>
      Relocation Services
    </p>
    <p class="contact contact--person">Daniel Hale<br>Director</p>
    <p class="contact contact--details">Tel : +123 555 0198<br>#27, Elm Avenue, Portland</p>
  </main>
</body>
</html>
```